Ice Cream Cup Design

We need a packaging design for ice cream cups.
We're a London based company called Villa Rosa Dolci and are producers of fresh Italian Artisan Gelato our website is www.villarosadolci.co.uk

We're looking to invest in a cup filling machine to fill 100ml and 500ml cups of gelato.
The 500ml cup will be the same shape and height as the Nordvik Freeze tub with a matching lid design.
The 100ml cup will be of the same shape and height of the Nordvik Freeze Single Serve cup with a matching lid design and includes a spoon inside.

We're looking for edgy clean designs that give an impression of quality and draw attention to the product if it sat on a product shelf. Inspired by packaging such as Ko, Pemberly and Harrowfield we're keen on a black themed packaging with a striking contrast of simple colour and a simple ice cream or gelato image that shows more than one flavour.
This particular design is not boasting any particular flavour, its a uniform design across our whole range of flavours.

Our company logo may be too fussy for this packaging so we would like to include our company ice cream logo and a way to include our company name but still look edgy for example - just like Pemberly Tea - our ice cream logo big G underneath, then 'VILLA ROSA DOLCI' underneath, and below that 'ARTISAN ITALIAN GELATO'. Or anything that inspires and looks good, will draw attention and looks sexy and indulgent and gives an impression of luxury product.

Please check attached document for cup shape and dimensions.

Reason: Christmas and New Year Holiday period resulted in less time for feedback opportunity and new designs to be posted.

Target Market(s)

Target market between 20-40 years old, consumers of quality desserts all year round.

Industry/Entity Type

It Company

Requirements
Must have
• Our Ice Cream Logo
Our name (doesn't need to necessarily have it in our font, can be in bold lettering)
Nice to have
• Limited writing and fuss.
Ideal to have simple clean designs
Should not have
• Eccentric colours and fun childlike images.

```html
<!DOCTYPE html>
<html lang="en">
<head>
<meta charset="utf-8">
<title>Villa Rosa Dolci – 500ml Gelato Tub Label</title>
<link rel="stylesheet" href="https://fonts.googleapis.com/css2?family=Lato:wght@300;400;700&display=swap">
<style>
  :root {
    --backdrop: #d4d4d4;
    --label-dark: #3a3a3c;
    --label-mid: #4a4a4d;
    --rose: #d63c74;
    --rose-light: #ec8fb0;
    --rose-deep: #b92a60;
    --ink-light: #f2f2f2;
  }
  * { margin: 0; padding: 0; box-sizing: border-box; }
  html, body {
    width: 1000px;
    height: 1200px;
    overflow: hidden;
    background: var(--backdrop);
    font-family: "Lato", sans-serif;
  }
  .tub-label {
    position: absolute;
    left: 100px;
    top: 150px;
    width: 800px;
    height: 900px;
    background: linear-gradient(90deg, var(--label-dark) 0%, var(--label-mid) 45%, var(--label-dark) 100%);
    overflow: hidden;
  }
  .lid-band {
    position: absolute;
    left: 0; top: 0;
    width: 100%;
    height: 120px;
    background: linear-gradient(90deg, var(--rose-deep) 0%, var(--rose) 40%, var(--rose-light) 75%, var(--rose) 100%);
  }
  .lid-band__rule {
    position: absolute;
    left: 0; top: 78px;
    width: 100%;
    height: 3px;
    background: var(--label-dark);
    opacity: 0.55;
  }
  .brand-seal {
    position: absolute;
    left: 50%;
    top: 18px;
    transform: translateX(-50%);
    display: flex;
    align-items: center;
    gap: 10px;
    padding: 0 18px;
    height: 44px;
    background: var(--rose);
    border-radius: 22px;
    border: 2px solid var(--label-dark);
  }
  .brand-seal__dot {
    width: 16px; height: 16px;
    border-radius: 50%;
    background: var(--ink-light);
  }
  .brand-seal__name {
    font-size: 16px;
    font-weight: 400;
    letter-spacing: 2px;
    color: var(--ink-light);
  }
  .splash {
    position: absolute;
    background: linear-gradient(90deg, var(--rose-deep), var(--rose-light));
  }
  .splash--upper {
    left: 300px; top: 262px;
    width: 250px; height: 60px;
    border-radius: 30px 30px 10px 10px;
  }
  .splash--lower {
    left: 235px; top: 520px;
    width: 360px; height: 240px;
    border-radius: 45% 55% 50% 50% / 40% 45% 60% 55%;
  }
  .wordmark {
    position: absolute;
    left: 0; top: 345px;
    width: 100%;
    text-align: center;
    color: var(--ink-light);
  }
  .wordmark__name {
    font-size: 70px;
    font-weight: 300;
    letter-spacing: 2px;
    line-height: 1;
  }
  .wordmark__tagline {
    margin-top: 6px;
    font-size: 30px;
    font-weight: 300;
    letter-spacing: 1px;
  }
  .volume-tag {
    position: absolute;
    left: 50%;
    bottom: 18px;
    transform: translateX(-50%);
    padding: 4px 8px;
    background: var(--rose);
    border: 2px solid #2c2c2e;
    font-size: 22px;
    font-weight: 700;
    color: var(--label-dark);
  }
</style>
</head>
<body>
  <main class="tub-label">
    <header class="lid-band">
      <div class="lid-band__rule"></div>
      <div class="brand-seal">
        <span class="brand-seal__dot"></span>
        <span class="brand-seal__name">VILLA ROSA DOLCI</span>
      </div>
    </header>

    <div class="splash splash--upper" role="img" aria-label="Pink gelato swirl splash illustration above the brand name"></div>

    <div class="wordmark">
      <h1 class="wordmark__name">VILLA ROSA DOLCI</h1>
      <p class="wordmark__tagline">ARTISAN ITALIAN GELATO</p>
    </div>

    <div class="splash splash--lower" role="img" aria-label="Pink gelato scoop splash illustration below the brand name"></div>

    <div class="volume-tag">500ml</div>
  </main>
</body>
</html>
```